New business blog needs wordpress theme

I need a unique wordpress theme for my new business oriented blog at quietharlan.net. The blog focuses on my experience as an entrepreneur and offers insights into business problems while chronicling my experience building a new company.

I would like to see a theme that looks more like a creative professional's website, not a business website. Large photos, bright colors, unique layout. I do not want stock photos of people in suits doing business type things. Also, no pictures of me - I am blogging anonymously.

The design should communicate technology and beauty - for example, I really like the feel of the landing page at www.plovel.com - it is beautiful to look at but also reflects the cutting edge nature of what they are doing.

Industry/Entity Type

Business

```html
<!DOCTYPE html>
<html lang="en">
<head>
<meta charset="utf-8">
<title>Quiet Harlan — Blog</title>
<link rel="stylesheet" href="https://fonts.googleapis.com/css2?family=Actor&family=Arimo:wght@400;700&display=swap">
<style>
:root{
  --page:#f1f1f1;
  --ink:#2b2b2b;
  --muted:#777;
  --soft:#9a9a9a;
  --accent:#33a3d8;
  --dark:#262629;
  --darker:#1b1b1d;
  --field:#2f2f33;
  --line:#dedede;
  --card:#ffffff;
}
*{box-sizing:border-box;margin:0;padding:0}
html,body{width:1200px;height:2161px;overflow:hidden}
body{background:var(--page);font-family:"Arimo",Arial,sans-serif;color:var(--ink);position:relative}
.abs{position:absolute}
a{color:var(--accent);text-decoration:none}

.topbar{left:120px;top:12px;width:960px;height:25px;background:var(--dark);color:#eee;font-size:11.5px;line-height:25px;padding-left:12px}
.topbar .social{position:absolute;right:54px;top:0;display:flex;gap:6px;align-items:center}
.topbar .social span{margin-right:6px;font-size:10px;letter-spacing:.3px}
.sq{display:inline-block;width:22px;height:20px;border:1px solid #bbb;border-radius:3px;background:#f4f4f4}
.topbar .close{position:absolute;right:0;top:0;width:34px;height:25px;background:#fff;border:1px solid var(--dark);color:var(--dark);text-align:center;font-weight:700;font-size:15px}

.brand{left:116px;top:64px;font-family:"Actor",sans-serif;font-size:54px;color:var(--ink);letter-spacing:.5px;white-space:nowrap}
.nav{left:566px;top:70px;display:flex;gap:30px}
.nav div{font-family:"Actor",sans-serif;font-size:19px;color:var(--ink);line-height:22px}
.nav small{display:block;font-family:"Arimo",sans-serif;font-size:10px;color:var(--accent);line-height:13px}

.pagetitle{left:118px;top:145px;font-family:"Actor",sans-serif;font-size:46px;color:var(--accent);line-height:50px}
.pagesub{left:120px;top:196px;font-size:11.5px;color:var(--muted)}
.search{left:784px;top:163px;width:231px;height:34px;background:var(--dark);color:#ddd;font-size:12px;line-height:34px;padding-left:22px}
.searchbtn{left:1024px;top:163px;width:40px;height:34px;background:var(--dark)}
.rule{left:120px;top:219px;width:960px;height:1px;background:var(--line)}
.vrule{left:760px;top:246px;width:1px;height:1445px;background:var(--line)}

.post{left:122px;width:598px;height:412px;background:var(--card);border:1px solid #ddd;box-shadow:0 12px 14px -8px rgba(0,0,0,.25)}
.post .photo{position:absolute;left:9px;top:9px;width:580px;height:234px}
.post.full .photo{left:0;top:0;width:596px;height:243px}
.post h2{position:absolute;left:44px;top:262px;font-family:"Actor",sans-serif;font-weight:400;font-size:20px;line-height:20px;color:var(--ink);letter-spacing:.3px;width:530px}
.post .meta{position:absolute;left:46px;font-size:11.5px;color:var(--ink)}
.post .excerpt{position:absolute;left:31px;width:545px;font-size:11.5px;line-height:19px;color:var(--soft)}
.post .share{position:absolute;left:0;bottom:0;width:100%;height:37px;border-top:1px solid #e4e4e4;background:#fafafa}
.post .share .icons{position:absolute;left:10px;top:8px;display:flex;gap:9px}
.post .share .next{position:absolute;right:9px;top:6px;width:26px;height:24px;background:var(--dark)}
.datebadge{width:64px;height:64px;border-radius:50%;background:var(--dark);color:#fff;text-align:center;font-family:"Actor",sans-serif}
.datebadge b{display:block;font-weight:400;font-size:13px;line-height:14px;margin-top:9px}
.datebadge strong{display:block;font-weight:400;font-size:25px;line-height:22px}
.datebadge i{display:block;font-style:normal;font-size:12px;line-height:12px}

.side h3{position:absolute;left:801px;font-family:"Actor",sans-serif;font-weight:400;font-size:20px;color:var(--ink)}
.tweet{left:801px;width:270px;font-size:11.5px;line-height:18px;color:var(--muted);padding-left:35px}
.tweet .dot{position:absolute;left:2px;top:5px;width:20px;height:14px;border-radius:50%;background:#555}
.tweet .dot.blue{background:var(--accent)}
.tweet em{display:block;color:var(--ink)}
.recent{left:801px;width:270px;height:78px;background:#fff;border:1px solid #d6d6d6;border-radius:3px;font-size:11.5px;line-height:18px;color:var(--ink);padding:10px 12px}
.recent .by{text-align:right;font-style:italic;margin-top:8px}
.recent:after{content:"";position:absolute;left:129px;bottom:-9px;width:14px;height:14px;background:#fff;border-right:1px solid #d6d6d6;border-bottom:1px solid #d6d6d6;transform:rotate(45deg)}
.toppost{left:801px;width:270px;height:92px;border-bottom:1px dashed #ccc}
.toppost .thumb{position:absolute;left:0;top:0;width:95px;height:69px;border:4px solid #fff;box-shadow:0 1px 4px rgba(0,0,0,.35)}
.toppost .txt{position:absolute;left:105px;top:0;font-size:11.5px;line-height:18px;color:var(--muted);width:165px}
.toppost .txt a{font-size:13px}
.listitem{left:801px;width:270px;height:30px;border-bottom:1px dashed #ccc;font-size:12.5px;color:var(--muted);padding-left:28px;line-height:22px}
.listitem .arr{position:absolute;left:0;top:6px;width:16px;height:11px;background:#777}
.listitem.on{color:var(--accent)}
.listitem.on .arr{background:var(--accent)}

.backtop{left:582px;top:1716px;width:36px;height:36px;border-radius:50%;background:var(--dark)}
.footrule{left:0;top:1733px;width:1200px;height:1px;background:var(--line)}
.footer{left:0;top:1773px;width:1200px;height:359px;background:var(--dark)}
.foot h4{position:absolute;top:1798px;font-family:"Actor",sans-serif;font-weight:400;font-size:20px;color:#eee;letter-spacing:.5px}
.foottext{left:120px;top:1835px;width:330px;font-size:12px;line-height:17px;color:#8a8a8e}
.gthumb{width:75px;height:75px;border:1px solid #3b3b3f}
.field{left:540px;width:220px;height:33px;background:var(--field);border-radius:2px;font-size:11px;color:#ddd;padding:10px 8px}
.field b{font-weight:700}
.field.msg{height:115px}
.sendbtn{left:582px;top:2041px;width:127px;height:27px;background:var(--field);color:#ddd;text-align:center;font-size:13px;line-height:27px}
.fpost{left:850px;width:260px;height:80px}
.fpost .thumb{position:absolute;left:0;top:0;width:95px;height:69px;border:3px solid #fff}
.fpost .txt{position:absolute;left:104px;top:0;font-size:11.5px;line-height:18px;color:#7d7d82;width:160px}
.fpost .txt a{font-size:13px}
.bottombar{left:0;top:2132px;width:1200px;height:29px;background:var(--darker);color:#ddd;font-size:11.5px;line-height:29px}
.bottombar .copy{position:absolute;left:120px}
.bottombar .links{position:absolute;right:144px;display:flex;gap:22px}
</style>
</head>
<body>

<div class="abs topbar">Harlan talks business. Best practices, articles and tips and about small business in the United States.
  <div class="social"><span>SOCIALIZE WITH US:</span><i class="sq"></i><i class="sq"></i><i class="sq"></i><i class="sq"></i><i class="sq"></i></div>
  <div class="close">✕</div>
</div>

<div class="abs brand">Quiet Harlan</div>
<nav class="abs nav">
  <div>HOME<small>Back Home</small></div>
  <div>FEATURES<small>Our best products</small></div>
  <div>PORTFOLIO<small>Our stuff on display</small></div>
  <div>BLOG<small>Our news</small></div>
  <div>CONTACT<small>Drop us a note</small></div>
</nav>

<div class="abs pagetitle">BLOG</div>
<div class="abs pagesub">Latest news from our blog, do check them out!</div>
<div class="abs search">Search</div>
<div class="abs searchbtn"><svg width="40" height="34" viewBox="0 0 40 34"><circle cx="18" cy="15" r="7" fill="none" stroke="#fff" stroke-width="2.2"/><line x1="23" y1="20" x2="28" y2="25" stroke="#fff" stroke-width="2.6"/></svg></div>
<div class="abs rule"></div>
<div class="abs vrule"></div>

<article class="abs post full" style="top:246px">
  <div class="photo" role="img" aria-label="Direct mail postcard beside a stack of colourful sale flyers" style="background:linear-gradient(100deg,#f4f4f2 0%,#ecebe6 45%,#d9c9a8 60%,#4fb3c9 78%,#e9e3d7 100%)"></div>
  <h2>Comparing Direct Mail to Dealhop – By the Numbers</h2>
  <div class="meta" style="top:291px">Posted on March 6, 2014 by <a>Harlan</a> <a>— Leave a comment</a></div>
  <div class="excerpt" style="top:310px">Lorem ipsum dolor sit amet, consectetuer adipiscing elit, sed diam nonummy nibh euismod tincidunt ut laoreet dolore magna aliquam erat volutpat. Ut wisi enim ad minim veniam, quis nostrud exerci tation ullamcorper suscipit lobortis nisl ut aliquip ex ea commodo consequat.</div>
  <div class="share"><div class="icons"><i class="sq"></i><i class="sq"></i><i class="sq"></i><i class="sq"></i><i class="sq"></i></div><div class="next"><svg width="26" height="24"><path d="M7 12h11M14 7l5 5-5 5" stroke="#fff" stroke-width="1.8" fill="none"/></svg></div></div>
</article>
<div class="abs datebadge" style="left:89px;top:496px"><b>Dec</b><strong>20</strong><i>2013</i></div>

<article class="abs post" style="top:713px">
  <div class="photo" role="img" aria-label="Screenshot of a daily deals website with a green promotion banner" style="background:linear-gradient(180deg,#4a4a4c 0%,#4a4a4c 19%,#4cc0de 19%,#4cc0de 27%,#eef3d8 27%,#9dcb5f 45%,#8cbf4f 100%)"></div>
  <h2>Finally Dumping Chatloop Calls on Pocketron –<br>Any Recommendations for an SMS App?</h2>
  <div class="meta" style="top:309px">Posted on March 6, 2014 by <a>Harlan</a> <a>— Leave a comment</a></div>
  <div class="excerpt" style="top:328px">Lorem ipsum dolor sit amet, consectetuer adipiscing elit, sed diam nonummy nibh euismod tincidunt ut laoreet dolore magna aliquam erat volutpat. Ut wisi enim ad minim</div>
  <div class="share"><div class="icons"><i class="sq"></i><i class="sq"></i><i class="sq"></i><i class="sq"></i><i class="sq"></i></div><div class="next"><svg width="26" height="24"><path d="M7 12h11M14 7l5 5-5 5" stroke="#fff" stroke-width="1.8" fill="none"/></svg></div></div>
</article>
<div class="abs datebadge" style="left:89px;top:963px"><b>Dec</b><strong>20</strong><i>2013</i></div>

<article class="abs post" style="top:1178px">
  <div class="photo" role="img" aria-label="Desert highway with a green road sign for gas, food and lodging" style="background:linear-gradient(180deg,#6d7fa3 0%,#a3aec4 40%,#8d8877 58%,#6d6a58 75%,#7a7670 100%)"></div>
  <h2>The Who &amp; The Why</h2>
  <div class="meta" style="top:291px">Posted on March 5, 2014 by <a>Harlan</a> <a>— 1 Comment</a></div>
  <div class="excerpt" style="top:310px">Lorem ipsum dolor sit amet, consectetuer adipiscing elit, sed diam nonummy nibh euismod tincidunt ut laoreet dolore magna aliquam erat volutpat. Ut wisi enim ad minim veniam, quis nostrud exerci tation ullamcorper suscipit lobortis nisl ut aliquip ex ea commodo consequat.</div>
  <div class="share"><div class="icons"><i class="sq"></i><i class="sq"></i><i class="sq"></i><i class="sq"></i><i class="sq"></i></div><div class="next"><svg width="26" height="24"><path d="M7 12h11M14 7l5 5-5 5" stroke="#fff" stroke-width="1.8" fill="none"/></svg></div></div>
</article>
<div class="abs datebadge" style="left:89px;top:1428px"><b>Dec</b><strong>20</strong><i>2013</i></div>

<aside class="side">
  <h3 style="top:238px">Latest Tweets</h3>
  <div class="abs tweet" style="top:271px"><i class="dot"></i>Lorem ipsum dolor sit amet, consectetuer adipiscing elit, sed diam nonummy nibh<br><a>http://hrl.to/trg87z</a><em>24 minutes ago</em></div>
  <div class="abs tweet" style="top:358px"><i class="dot"></i>Lorem ipsum dolor sit amet, consectetuer adipiscing elit, sed diam nonummy nibh<br><a>http://hrl.to/trg87z</a><em>24 minutes ago</em></div>
  <div class="abs tweet" style="top:444px"><i class="dot blue"></i>Lorem ipsum dolor sit amet, consectetuer adipiscing elit, sed diam nonummy nibh<br><a>http://hrl.to/trg87z</a><em>24 minutes ago</em></div>

  <h3 style="top:530px;left:806px">Recent Posts</h3>
  <div class="abs recent" style="top:566px">Lorem ipsum dolor sit amet, consectetuer adipiscing elit, sed diam nonummy nibh...<div class="by">by Tomlin on <a>Some Demo post</a></div></div>
  <div class="abs recent" style="top:681px">Lorem ipsum dolor sit amet, consectetuer adipiscing elit, sed diam nonummy nibh...<div class="by">by Tomlin on <a>Some Demo post</a></div></div>
  <div class="abs recent" style="top:796px">Lorem ipsum dolor sit amet, consectetuer adipiscing elit, sed diam nonummy nibh...<div class="by">by Tomlin on <a>Some Demo post</a></div></div>

  <h3 style="top:910px">Top Posts by Clicks</h3>
  <div class="abs toppost" style="top:948px"><div class="thumb" role="img" aria-label="Red fruit close-up" style="background:radial-gradient(circle at 55% 50%,#d8321f,#5a0d08)"></div><div class="txt"><a>This is a sample Post 1</a><br>Lorem ipsum dolor sit amet, consectetuer adipiscing elit, sed diam nonummy nibh...</div></div>
  <div class="abs toppost" style="top:1048px"><div class="thumb" role="img" aria-label="Strawberry on white" style="background:radial-gradient(circle at 50% 55%,#d7302a,#f3eeea 70%)"></div><div class="txt"><a>This is a sample Post 1</a><br>Lorem ipsum dolor sit amet, consectetuer adipiscing elit, sed diam nonummy nibh...</div></div>
  <div class="abs toppost" style="top:1148px"><div class="thumb" role="img" aria-label="Black and white flower" style="background:radial-gradient(circle at 50% 50%,#bbb,#222)"></div><div class="txt"><a>This is a sample Post 1</a><br>Lorem ipsum dolor sit amet, consectetuer adipiscing elit, sed diam nonummy nibh...</div></div>

  <h3 style="top:1252px">Blog Categories</h3>
  <div class="abs listitem" style="top:1290px"><i class="arr"></i>Blog Category 1 (5)</div>
  <div class="abs listitem" style="top:1324px"><i class="arr"></i>Blog Category 2 (3)</div>
  <div class="abs listitem on" style="top:1357px"><i class="arr"></i>Blog Category 3 (8)</div>
  <div class="abs listitem" style="top:1391px"><i class="arr"></i>Blog Category 4 (12)</div>
  <div class="abs listitem" style="top:1425px"><i class="arr"></i>Blog Category 5 (7)</div>

  <h3 style="top:1470px">Archives</h3>
  <div class="abs listitem" style="top:1500px"><i class="arr"></i>January 2012 (23)</div>
  <div class="abs listitem" style="top:1534px"><i class="arr"></i>December 2011 (34)</div>
  <div class="abs listitem on" style="top:1567px"><i class="arr"></i>November 2011 (21)</div>
  <div class="abs listitem" style="top:1601px"><i class="arr"></i>October 2011 (11)</div>
  <div class="abs listitem" style="top:1635px"><i class="arr"></i>September 2011 (44)</div>
  <div class="abs listitem" style="top:1668px;border:0"><i class="arr"></i>August 2011 (4)</div>
</aside>

<div class="abs footrule"></div>
<div class="abs backtop"><svg width="36" height="36"><path d="M12 21l6-6 6 6" stroke="#fff" stroke-width="2" fill="none"/></svg></div>

<footer class="foot">
  <div class="abs footer"></div>
  <h4 style="left:120px">SNAPLY GALLERY</h4>
  <div class="abs foottext">Hover to highlight images. Lorem ipsum dolor sit amet, consectetur adipisicing elit, sed do eiusmod tempor.</div>
  <div class="abs gthumb" role="img" aria-label="Gallery photo" style="left:120px;top:1887px;background:#4a4538"></div>
  <div class="abs gthumb" role="img" aria-label="Gallery photo" style="left:202px;top:1887px;background:#3f4a40"></div>
  <div class="abs gthumb" role="img" aria-label="Gallery photo" style="left:284px;top:1887px;background:#5a6a45"></div>
  <div class="abs gthumb" role="img" aria-label="Gallery photo" style="left:366px;top:1887px;background:#4a2a2a"></div>
  <div class="abs gthumb" role="img" aria-label="Gallery photo" style="left:120px;top:1969px;background:#3b3a3c"></div>
  <div class="abs gthumb" role="img" aria-label="Gallery photo" style="left:202px;top:1969px;background:linear-gradient(#c9914a,#6a4a2a)"></div>
  <div class="abs gthumb" role="img" aria-label="Gallery photo" style="left:284px;top:1969px;background:#4a4030"></div>
  <div class="abs gthumb" role="img" aria-label="Gallery photo" style="left:366px;top:1969px;background:#3e3530"></div>

  <h4 style="left:539px">GET IN TOUCH</h4>
  <div class="abs field" style="top:1837px"><b>Email</b> (required)</div>
  <div class="abs field" style="top:1876px"><b>Email</b> (required)</div>
  <div class="abs field msg" style="top:1916px"><b>Message</b> (required)</div>
  <div class="abs sendbtn">Send Message</div>

  <h4 style="left:848px">LATEST POSTS</h4>
  <div class="abs fpost" style="top:1832px"><div class="thumb" role="img" aria-label="Snowy mountain under blue sky" style="background:linear-gradient(#2d5ea8,#9ab4d6 60%,#3a4a5a)"></div><div class="txt"><a>This is a sample Post 1</a><br>Lorem ipsum dolor sit amet, consectetuer adipiscing elit, sed diam nonummy nibh...</div></div>
  <div class="abs fpost" style="top:1933px"><div class="thumb" role="img" aria-label="Green macro nature shot" style="background:radial-gradient(circle,#c9d6a0,#3f6a22)"></div><div class="txt"><a>This is a sample Post 1</a><br>Lorem ipsum dolor sit amet, consectetuer adipiscing elit, sed diam nonummy nibh...</div></div>
  <div class="abs fpost" style="top:2034px"><div class="thumb" role="img" aria-label="Colourful paint brush" style="background:linear-gradient(120deg,#d23aa8,#f05a9a 50%,#6a3ac0)"></div><div class="txt"><a>This is a sample Post 1</a><br>Lorem ipsum dolor sit amet, consectetuer adipiscing elit, sed diam nonummy nibh...</div></div>
</footer>

<div class="abs bottombar">
  <div class="copy">© 2014 www.companyname.com | powered by SteadyHostWorks</div>
  <div class="links"><span>HOME</span><span>FEATURES</span><span>CONTACT</span><span>FORUM</span></div>
</div>

</body>
</html>
```